Verdalux Web Presence

I need a word press site for my company that houses diverse services, and am looking to profile these areas: Design and Delivery of Social Innovation Initiatives, Innovative Pubic Engagement, The Turquoise Economy, Youth Entrepreneurship, and The Science of Change.

I would also like to profile my recent projects. A blog, video and photos are also important features.

Industry/Entity Type

It Company

Requirements
Must have
• I would like to have an overview of what the company does as a Think, Feel and Do Company, along with sections for specific services and recent project profiles.

I would like a section for a blog

I would like a section for photos and video.

I would like the look and feel of the website to reflect the following:

Morwen has spent 30 years leading expeditions into the future. Morwen has a special interest in exploring the changing business, social and cultural landscapes and frontiers, uncovering uncharted territory and unleashing hidden potential – within the person, family, organization, community, business or marketplace. Morwen thrives on experimentation that has led to blended eastern and western methodologies and technologies that help people and organizations deal with the chronic and tough issues in research-based, intelligent and inspiring ways.

Specialties:Breaking down the walls between disciplines such as environmental, social, and economic approaches to create ideologies and methodologies that weave them all to change the way we live. This ideology and methodology applies to all areas: business development, business identity, strategy for all organizations - public, private and NGO.This starts at the individual level.Morwen is also an energy healer specializing in belief reconstruction leading to fulfilling lives.

```html
<!DOCTYPE html>
<html lang="en">
<head>
<meta charset="utf-8">
<title>Verdalux</title>
<link href="https://fonts.googleapis.com/css2?family=Roboto:wght@300;400;500;700&family=Varela+Round&display=swap" rel="stylesheet">
<style>
:root{
  --blue:#1a5cae;
  --blue-light:#5aaee0;
  --yellow:#f2c81c;
  --yellow-dark:#e1b512;
  --red:#ef3d36;
  --red-dark:#d92f29;
  --teal:#0f8c7b;
  --teal-dark:#0a7a6a;
  --orange:#f08a24;
  --orange-dark:#de7a16;
  --ink:#333;
  --text:#555;
  --band:#ececec;
  --footer:#2a2a2a;
  --white:#fff;
}
*{margin:0;padding:0;box-sizing:border-box}
html,body{width:1016px;height:1200px;overflow:hidden;background:var(--white)}
body{position:relative;font-family:"Roboto",Arial,sans-serif;color:var(--text)}
.abs{position:absolute}

.hero{left:96px;top:0;width:820px;height:432px;
  background:
    radial-gradient(ellipse 170px 150px at 56% 70%,rgba(40,52,78,.55),rgba(40,52,78,0) 100%),
    radial-gradient(ellipse 110px 120px at 18% 62%,rgba(70,76,86,.35),rgba(70,76,86,0) 100%),
    radial-gradient(ellipse 260px 160px at 30% 35%,rgba(150,200,130,.45),rgba(150,200,130,0) 100%),
    radial-gradient(ellipse 240px 170px at 80% 30%,rgba(140,190,125,.45),rgba(140,190,125,0) 100%),
    linear-gradient(180deg,#f4f8f1 0%,#e6efe0 60%,#f2f0ea 100%);
  -webkit-mask-image:linear-gradient(90deg,transparent 0,#000 6%,#000 94%,transparent 100%);
  mask-image:linear-gradient(90deg,transparent 0,#000 6%,#000 94%,transparent 100%)}
.brand{left:174px;top:40px;font-weight:300;font-size:34px;color:var(--blue);letter-spacing:.5px;display:flex;align-items:center;gap:8px}
.brand .dot{width:10px;height:10px;border-radius:50%;background:var(--red)}

.nav{left:169px;top:411px;width:678px;height:36px;background:var(--white);box-shadow:0 2px 4px rgba(0,0,0,.12);display:flex;align-items:center}
.nav a{font-size:11.5px;font-weight:500;color:var(--ink);text-decoration:none;padding:0 11px;height:36px;line-height:36px}
.nav a.active{background:var(--blue);color:var(--white)}
.social{margin-left:auto;display:flex;gap:12px;padding-right:16px}
.social span{width:10px;height:10px;border-radius:50%;background:var(--blue)}

.welcome-title{left:172px;top:474px;font-family:"Varela Round",sans-serif;font-size:25px;font-weight:400;color:var(--blue-light)}
.welcome-rule{left:293px;top:472px;width:1px;height:38px;background:#ddd}
.welcome-text{left:306px;top:471px;width:532px;font-size:9.8px;line-height:13px;color:var(--text)}
.learn{font-size:11px;color:var(--blue);text-decoration:none}
.welcome-more{left:305px;top:519px}
.dotted{left:0;top:550px;width:1016px;border-top:1px dotted #ccc}

.band{left:0;top:644px;width:1016px;height:282px;background:var(--band)}
.services{left:169px;top:572px;width:678px;height:135px;overflow:hidden}
.track{display:flex;gap:14px;width:max-content}
.card{position:relative;width:159px;height:135px;color:var(--white);flex:none}
.card h3{height:29px;line-height:29px;font-size:12px;font-weight:700;padding-left:9px;letter-spacing:-.2px;white-space:nowrap}
.card p{font-size:8.4px;line-height:11.5px;padding:8px 9px 0}
.card .learn{position:absolute;left:9px;top:111px;color:rgba(255,255,255,.75)}
.c1{background:var(--blue)} .c1 h3{background:var(--blue)}
.c2{background:var(--yellow)} .c2 h3{background:var(--yellow-dark)}
.c3{background:var(--red)} .c3 h3{background:var(--red-dark)}
.c4{background:var(--teal)} .c4 h3{background:var(--teal-dark)}
.c5{background:var(--orange)} .c5 h3{background:var(--orange-dark)}
.shadow-line{left:169px;top:720px;width:678px;height:4px;background:radial-gradient(ellipse at center,rgba(0,0,0,.15),rgba(0,0,0,0) 70%)}

.section-title{font-size:18.5px;font-weight:700;color:var(--ink);letter-spacing:-.6px}
.section-title b{color:var(--blue)}
.proj-title{left:168px;top:748px}
.proj-img{top:782px;width:139px;height:89px;border:2px solid #fff;box-shadow:0 0 0 1px #bbb}
.proj-cap{top:876px;width:150px;font-size:12px;font-weight:700;line-height:16px;color:var(--ink)}
.divider{left:618px;top:752px;width:1px;height:156px;background:#ccc}
.blog-title{left:629px;top:748px}
.blog-thumb{left:630px;width:35px;height:35px;border:2px solid #fff;box-shadow:0 0 0 1px #bbb;background:linear-gradient(135deg,#8a8f99,#3a3f4a)}
.blog-text{left:676px;width:166px;font-size:10.5px;font-weight:500;line-height:14px;color:var(--ink)}

.gallery{left:0;top:926px;width:1016px;height:176px;background:var(--blue)}
.gallery-title{left:169px;top:944px;font-size:18.5px;font-weight:700;color:var(--white);letter-spacing:-.6px}
.gal-img{top:975px;width:128px;height:104px;border:1px solid rgba(255,255,255,.5)}

.footer{left:0;top:1102px;width:1016px;height:52px;background:var(--footer)}
.foot-nav{left:172px;top:1124px;display:flex;gap:27px}
.foot-nav a{font-size:8.5px;color:#aaa;text-decoration:none}
.foot-brand{left:754px;top:1114px;font-weight:300;font-size:21px;color:#555}
.copyright{left:173px;top:1172px;font-size:8px;color:#999}
.copyright a{color:var(--blue);text-decoration:none}
.foot-social{left:774px;top:1172px;display:flex;gap:17px}
.foot-social span{width:10px;height:10px;border-radius:50%;background:var(--blue)}
</style>
</head>
<body>
<div class="abs hero" role="img" aria-label="Photo of a businessman in a suit at a laptop, colleagues talking in a bright green office behind him"></div>
<div class="abs brand"><span>Verdalux</span><span class="dot"></span></div>

<nav class="abs nav">
  <a class="active" href="#">HOME</a><a href="#">ABOUT US</a><a href="#">PRODUCTS</a><a href="#">SERVICES</a><a href="#">BLOG</a><a href="#">SUPPORT</a><a href="#">CONTACT</a>
  <div class="social" aria-label="Social links"><span></span><span></span><span></span></div>
</nav>

<h1 class="abs welcome-title">welcome</h1>
<div class="abs welcome-rule"></div>
<p class="abs welcome-text">Vivamus lacus neque, euismod vitae elementum sed, rutrum a turpis. Suspendisse fringilla quam a eleifend aliquet. Nulla facilisi. Praesent quam arcu, scelerisque eget luctus ac, dignissim eget ipsum. Praesent varius nibh ac nulla aliquam convallis. Ut tincidunt luctus nisi vitae malesuada.</p>
<a class="abs learn welcome-more" href="#">&gt;&gt;LEARN MORE</a>
<div class="abs dotted"></div>

<div class="abs band"></div>
<svg class="abs" style="left:140px;top:624px" width="22" height="42" viewBox="0 0 22 42"><polyline points="20,1 2,21 20,41" fill="none" stroke="#999" stroke-width="1.2"/></svg>
<svg class="abs" style="left:856px;top:624px" width="22" height="42" viewBox="0 0 22 42"><polyline points="2,1 20,21 2,41" fill="none" stroke="#999" stroke-width="1.2"/></svg>

<section class="abs services" aria-label="Services">
  <div class="track">
    <article class="card c1"><h3>SOCIAL INNOVATION</h3><p>Vivamus lacus neque, euismod vitae elementum sed, rutrum a turpis. Suspendisse fringilla quam a eleifend aliquet. Nulla facilisi. Praesent quam arcu, scelerisque eget luctus ac.</p><a class="learn" href="#">&gt;&gt;LEARN MORE</a></article>
    <article class="card c2"><h3>PUBIC ENGAGEMENT</h3><p>Vivamus lacus neque, euismod vitae elementum sed, rutrum a turpis. Suspendisse fringilla quam a eleifend aliquet. Nulla facilisi. Praesent quam arcu, scelerisque eget luctus ac.</p><a class="learn" href="#">&gt;&gt;LEARN MORE</a></article>
    <article class="card c3"><h3>TURQUOISE ECONOMY</h3><p>Vivamus lacus neque, euismod vitae elementum sed, rutrum a turpis. Suspendisse fringilla quam a eleifend aliquet. Nulla facilisi. Praesent quam arcu, scelerisque eget luctus ac.</p><a class="learn" href="#">&gt;&gt;LEARN MORE</a></article>
    <article class="card c4"><h3>SCIENCE OF CHANGE</h3><p>Vivamus lacus neque, euismod vitae elementum sed, rutrum a turpis. Suspendisse fringilla quam a eleifend aliquet. Nulla facilisi. Praesent quam arcu, scelerisque eget luctus ac.</p><a class="learn" href="#">&gt;&gt;LEARN MORE</a></article>
    <article class="card c5"><h3>YOUTH ENTREPRENEURSHIP</h3><p>Vivamus lacus neque, euismod vitae elementum sed, rutrum a turpis. Suspendisse fringilla quam a eleifend aliquet. Nulla facilisi. Praesent quam arcu, scelerisque eget luctus ac.</p><a class="learn" href="#">&gt;&gt;LEARN MORE</a></article>
  </div>
</section>
<div class="abs shadow-line"></div>

<h2 class="abs section-title proj-title"><b>RECENT</b> PROJECTS</h2>
<div class="abs proj-img" style="left:170px;background:linear-gradient(135deg,#f3c640,#d99a1c)" role="img" aria-label="Drafting tools and pencil on a yellow plan"></div>
<div class="abs proj-img" style="left:319px;background:linear-gradient(135deg,#e8e6e2,#c9402f 60%,#e9e9e9)" role="img" aria-label="Pens and charts on a desk"></div>
<div class="abs proj-img" style="left:468px;background:linear-gradient(135deg,#c7d4e6,#8ea3c0 60%,#f0c020)" role="img" aria-label="Blueprint with hard hat, hammer and tape measure"></div>
<p class="abs proj-cap" style="left:170px">Vivamus lacus neque, euismod vitae.</p>
<p class="abs proj-cap" style="left:319px">Elementum sed,<br>rutrum a turpis.</p>
<p class="abs proj-cap" style="left:468px">Nulla facilisi. Praesent quam arcu.</p>

<div class="abs divider"></div>
<h2 class="abs section-title blog-title"><b>LATEST</b> BLOGPOSTS</h2>
<div class="abs blog-thumb" style="top:781px" role="img" aria-label="Team meeting thumbnail"></div>
<div class="abs blog-thumb" style="top:823px" role="img" aria-label="Business discussion thumbnail"></div>
<div class="abs blog-thumb" style="top:866px" role="img" aria-label="Office worker thumbnail"></div>
<p class="abs blog-text" style="top:781px">Vivamus lacus neque, euismod vitae elementum sed.</p>
<p class="abs blog-text" style="top:824px">Vivamus lacus neque, euismod vitae elementum sed.</p>
<p class="abs blog-text" style="top:866px">Vivamus lacus neque, euismod vitae elementum sed.</p>

<div class="abs gallery"></div>
<h2 class="abs gallery-title">GALLERY</h2>
<svg class="abs" style="left:140px;top:1002px" width="22" height="44" viewBox="0 0 22 44"><polyline points="20,1 2,22 20,43" fill="none" stroke="#fff" stroke-width="1.5"/></svg>
<svg class="abs" style="left:856px;top:1002px" width="22" height="44" viewBox="0 0 22 44"><polyline points="2,1 20,22 2,43" fill="none" stroke="#fff" stroke-width="1.5"/></svg>
<div class="abs gal-img" style="left:169px;background:linear-gradient(135deg,#b08a60,#5a4634)" role="img" aria-label="Construction workers reviewing plans"></div>
<div class="abs gal-img" style="left:307px;background:linear-gradient(135deg,#a86a50,#3a2a24)" role="img" aria-label="Smiling woman portrait"></div>
<div class="abs gal-img" style="left:444px;background:linear-gradient(135deg,#6a6a6a,#1e1e1e)" role="img" aria-label="Team around a conference table"></div>
<div class="abs gal-img" style="left:582px;background:radial-gradient(circle,#6a4a30,#1e1410)" role="img" aria-label="Video of a meeting seen from above"></div>
<svg class="abs" style="left:626px;top:1007px" width="40" height="40" viewBox="0 0 40 40"><circle cx="20" cy="20" r="18" fill="#e8e8e8" stroke="#999" stroke-width="2"/><polygon points="16,12 28,20 16,28" fill="#222"/></svg>
<div class="abs gal-img" style="left:719px;background:linear-gradient(135deg,#c8a890,#3a302a)" role="img" aria-label="Thoughtful young man portrait"></div>

<footer class="abs footer"></footer>
<nav class="abs foot-nav"><a href="#">HOME</a><a href="#">ABOUT US</a><a href="#">PRODUCTS</a><a href="#">SERVICES</a><a href="#">BLOG</a><a href="#">SUPPORT</a><a href="#">CONTACT</a></nav>
<div class="abs foot-brand">Verdalux</div>
<p class="abs copyright">Copyright © 2013 Verdalux. All rights reserved. &nbsp; <a href="#">Privacy Policy</a> &nbsp;|&nbsp; <a href="#">Terms of Use</a></p>
<div class="abs foot-social" aria-label="Social links"><span></span><span></span><span></span></div>
</body>
</html>
```